Mini-Banner für Rubriken
Hallo,
wir benötigen für unsere Seite www.quilmar.de neue und vorallem passende Banner für die Highlights (rechte Seite) innerhalb der Rubriken, wie z.B. All Inklusive, Wellness, Urlaub an der Küste u.s.w. Vielen Dank für die Vorschläge !

```html
<!DOCTYPE html>
<html lang="de">
<head>
<meta charset="utf-8">
<title>quilmar Deutschlandreisen</title>
<link href="https://fonts.googleapis.com/css2?family=Open+Sans:wght@400;700&family=Kaushan+Script&display=swap" rel="stylesheet">
<style>
:root{
  --page-blue:#1c72c6;
  --frame:#ffffff;
  --green:#7dc242;
  --panel:#f2f2f2;
  --panel-head:#e2e2e2;
  --border:#c9c9c9;
  --red:#8b1a1a;
  --price:#8b0000;
  --text:#333333;
  --link:#7a1010;
  --top-green:#2e9b2e;
  --alert:#ff1a1a;
}
*{box-sizing:border-box;margin:0;padding:0}
html,body{width:1200px;height:929px;overflow:hidden}
body{background:var(--page-blue);font-family:"Open Sans",Verdana,sans-serif;color:var(--text);position:relative}
.frame{position:absolute;left:103px;top:13px;width:1002px;height:940px;background:var(--frame);border-radius:18px 18px 0 0}
.header{position:absolute;left:110px;top:18px;width:988px;height:124px;border-radius:14px 14px 0 0;overflow:hidden}
.header-logo{position:absolute;left:0;top:0;width:226px;height:96px;background:linear-gradient(#e9f1f8,#cfdde9)}
.brand{position:absolute;left:30px;top:40px;font-weight:700;font-size:34px;color:var(--green);letter-spacing:-1px}
.brand small{font-size:13px;color:#1f6fb8}
.header-banner{position:absolute;left:226px;top:0;width:762px;height:96px;background:linear-gradient(90deg,#b7cce2,#dfe8f2 45%,#aac3dc)}
.slogan{position:absolute;left:305px;top:18px;font-weight:700;font-style:italic;font-size:25px;color:#fff}
.slogan2{position:absolute;left:290px;top:50px;font-weight:700;font-style:italic;font-size:25px;color:#f28a1a}
.header-bar{position:absolute;left:0;top:96px;width:988px;height:28px;background:linear-gradient(90deg,var(--green),#9fd35c 60%,#cfe8a8)}
.header-bar .region{position:absolute;left:22px;top:1px;font-weight:700;font-style:italic;font-size:17px;color:#fff}
.header-nav{position:absolute;left:512px;top:5px;display:flex;gap:20px;font-weight:700;font-size:13px;color:#111}
.box{position:absolute;background:var(--panel);border:1px solid var(--border);border-radius:6px 6px 0 0;font-size:12px}
.box-head{height:26px;background:linear-gradient(#f3f3f3,var(--panel-head));border-bottom:1px solid var(--border);border-radius:6px 6px 0 0;text-align:center;font-weight:700;font-size:12.5px;line-height:26px;color:#111}
.menu{list-style:none;padding:10px 8px;line-height:15.5px}
.menu li::before{content:"• ";color:var(--red)}
.menu li{color:var(--link)}
.menu .gap{height:15px}
.menu .gap::before{content:""}
.menu .top{color:var(--top-green);font-weight:700}
.social{display:flex;gap:8px;padding:0 10px}
.social span{width:44px;height:44px;border-radius:5px}
.voucher{margin:0 auto;width:204px;height:100px;background:linear-gradient(135deg,#a4161c,#c12a2f 50%,#8e1014);display:flex;align-items:center;justify-content:center;font-family:"Kaushan Script",cursive;font-size:30px;color:#fff}
.main{position:absolute;left:334px;top:149px;width:531px;height:800px;background:#fafafa;border:1px dotted #aaa;border-radius:6px}
.offer{position:absolute;left:14px;width:505px}
.offer h2{font-size:15px;font-weight:700;color:var(--red);line-height:19px}
.offer h3{font-size:12.5px;font-weight:700;color:var(--red);line-height:17px}
.offer p{position:absolute;font-size:11px;line-height:15px;color:#333}
.photo{position:absolute;border-radius:4px}
.from{position:absolute;font-size:11.5px;font-weight:700;color:var(--red)}
.price{position:absolute;font-size:19px;font-weight:700;color:var(--price)}
.more{position:absolute;width:135px;height:21px;background:linear-gradient(#9a2a2a,#6e1414);color:#fff;font-weight:700;font-size:12px;text-align:center;line-height:21px;border-radius:2px}
.divider{position:absolute;left:0;width:531px;border-top:2px solid #666}
.highlight{display:block;margin:0 3px 8px;width:198px;height:62px;border-radius:6px;position:relative;overflow:hidden}
.highlight b,.highlight i{position:absolute;font-family:"Kaushan Script",cursive;font-weight:400;font-style:normal;color:#c8102e}
.highlight b{right:8px;top:4px;font-size:20px}
.highlight i{left:6px;bottom:4px;font-size:17px}
.filter{padding:0 14px;font-size:12px;color:#222}
.filter label{display:block;margin:10px 0 5px}
.select{height:18px;border:1px solid #aaa;border-radius:4px;background:linear-gradient(#fff,#e8e8e8);font-size:11px;padding-left:10px;line-height:16px}
.btn{margin-top:8px;height:22px;border:1px solid #aaa;border-top-color:var(--red);background:#fff;text-align:center;font-size:12px;line-height:20px}
.or{text-align:center;font-weight:700;margin-top:6px}
.offer-no{height:21px;background:var(--alert);color:#fff;text-align:center;font-weight:700;font-size:12px;line-height:21px;margin:2px -3px 0}
.field{margin-top:6px;width:148px;height:21px;border:1px solid #ccc;border-bottom-color:var(--red);background:#fff}
</style>
</head>
<body>
<div class="frame"></div>

<header class="header">
  <div class="header-logo" role="img" aria-label="Verschneite Winterbäume hinter dem Markennamen">
    <div class="brand">quilmar<small>.de</small></div>
  </div>
  <div class="header-banner" role="img" aria-label="Winterliche Berglandschaft mit Schneemann und Familie im Schnee">
    <div class="slogan">Zeit zu reisen...</div>
    <div class="slogan2">...unsere Winter-Specials</div>
  </div>
  <div class="header-bar">
    <span class="region">Deutschlandreisen</span>
    <nav class="header-nav"><span>Kontakt</span><span>Impressum</span><span>AGB</span></nav>
  </div>
</header>

<aside class="box" style="left:110px;top:152px;width:204px;height:138px">
  <div class="box-head"></div>
  <ul class="menu"><li>Startseite</li><li>Alle Hotels</li></ul>
  <div class="social">
    <span style="background:#c4171b" role="img" aria-label="Videokanal"></span>
    <span style="background:#2d5a9e" role="img" aria-label="Netzwerk"></span>
  </div>
</aside>

<aside class="box" style="left:110px;top:304px;width:204px;height:262px">
  <div class="box-head">Kategorien</div>
  <ul class="menu">
    <li class="top">Topseller</li><li class="gap"></li>
    <li>Last Minute</li><li>Städtereisen</li><li>Familienurlaub</li><li>Wellness</li><li>Gruppenreisen</li><li>All Inklusive</li><li>Ferienwohnungen</li><li>Relaxen &amp; Erholung</li><li>Fest &amp; Feiertage</li><li>love &amp; romance</li><li class="gap"></li><li>Alle Angebote</li>
  </ul>
</aside>

<aside class="box" style="left:110px;top:580px;width:204px;height:135px">
  <div class="box-head">Gutschein schenken</div>
  <div class="voucher" role="img" aria-label="Roter Geschenkgutschein mit Schriftzug">Gutschein</div>
</aside>

<aside class="box" style="left:110px;top:729px;width:204px;height:81px">
  <div class="box-head"></div>
  <ul class="menu"><li>Rückruf anfordern</li><li>Anfrage stellen</li></ul>
</aside>

<aside class="box" style="left:110px;top:824px;width:204px;height:120px">
  <div class="box-head">Newsletter</div>
  <p style="padding:12px 8px;line-height:15px">Bleiben Sie immer auf dem neuesten Stand. Tragen Sie sich jetzt für unseren Newsletter ein.</p>
</aside>

<main class="main">
  <article class="offer" style="top:16px;height:220px">
    <h2>ALL INKLUSIVE Urlaub im schönen Erzgebirge</h2>
    <h3>5 Tage / 4 Übernachtungen mit Vollpension + Getränke All Inklusive v. 11-22.30 Uhr !</h3>
    <p style="left:3px;top:74px;width:228px">Wir erwarten Sie im ersten echten ALL INKLUSIV HOTEL im Erzgebirge. Unser modernes Designer Hotel entspricht den Erwartungen eines 4 Sterne Hauses. Gr...</p>
    <span class="from" style="left:5px;top:168px">schon ab</span>
    <span class="price" style="left:88px;top:161px">196,00 € p.P.</span>
    <span class="more" style="left:97px;top:194px">mehr Infos...!</span>
    <div class="photo" role="img" aria-label="Hotelgebäude mit Fensterläden" style="left:248px;top:70px;width:233px;height:140px;background:linear-gradient(#eef1f4,#d8d4cc 60%,#8a9a6a)"></div>
  </article>
  <div class="divider" style="top:253px"></div>

  <article class="offer" style="top:270px;height:240px">
    <h2>BEAUTY &amp; WELLNESSTAGE inkl. Vollpension + ALL Inklusive Getränke</h2>
    <h3>4 Tage im Erzgebirge inkl. Kosmetikbehandlung von 30 min. uvm.</h3>
    <div class="photo" role="img" aria-label="Grünes Blatt mit weißer Pflegecreme" style="left:0;top:72px;width:233px;height:140px;background:linear-gradient(160deg,#dff0f2,#7ec860 45%,#f4f6f4 80%)"></div>
    <p style="left:273px;top:74px;width:230px">Bei uns ist der Kunde noch König. Verbringen Sie ein paar erholsame Tage im ersten ECHT ALL INKLUSIVE HOTEL mitten im schönen Erzgebirge.</p>
    <span class="from" style="left:279px;top:152px">schon ab</span>
    <span class="price" style="left:358px;top:145px">179,00 € p.P.</span>
    <span class="more" style="left:368px;top:178px">mehr Infos...!</span>
  </article>
  <div class="divider" style="top:494px"></div>

  <article class="offer" style="top:511px;height:240px">
    <h2>Die perfekte Geschenkidee für Ihren Schatz</h2>
    <h3>3 Tage im Erzgebirge inkl. Vollpension und von 11.00- 22.30 Uhr Getränke</h3>
    <p style="left:3px;top:71px;width:228px">Verbringen Sie ein paar erholsame Tage im schönen Erzgebirge. Unsere reizvolle Umgebung bietet Ihnen eine Vielzahl an Sehenswürdigkeiten. Ob eine Be...</p>
    <span class="from" style="left:5px;top:150px">schon ab</span>
    <span class="price" style="left:98px;top:143px">98,00 € p.P.</span>
    <span class="more" style="left:97px;top:176px">mehr Infos...!</span>
    <div class="photo" role="img" aria-label="Festlich gedeckter Speisesaal mit Buffet" style="left:248px;top:67px;width:233px;height:140px;background:linear-gradient(#c88a3a,#7a3a1a 55%,#e8d8c0)"></div>
  </article>
  <div class="divider" style="top:731px"></div>

  <article class="offer" style="top:746px">
    <h2>Erholsame Tage nur unter Frauen !!! - Wellness</h2>
    <h3>3 Tage im schönen Erzgebirge inkl. Wellnessanwendungen</h3>
  </article>
</main>

<aside class="box" style="left:891px;top:152px;width:204px;height:656px">
  <div class="box-head">Highlights</div>
  <div style="padding-top:7px">
    <a class="highlight" role="img" aria-label="Banner All Inclusive im Erzgebirge mit Buffet" style="background:linear-gradient(90deg,#8a4a2a,#e8c89a 55%,#f2efe8)"><b>All Inclusive</b><i>im Erzgebirge</i></a>
    <a class="highlight" role="img" aria-label="Banner Erholungsurlaub im Harz mit Landschaft" style="background:linear-gradient(90deg,#a8c8dc,#dfe8ee 50%,#7aa05a)"><b>Erholungsurlaub</b><i>im Harz</i></a>
    <a class="highlight" role="img" aria-label="Banner Wellnessurlaub in Bayern mit Massage" style="background:linear-gradient(90deg,#f4e2d6,#fbf1ea 55%,#e2b6a0)"><b>Wellnessurlaub</b><i>in Bayern</i></a>
    <a class="highlight" role="img" aria-label="Banner Erholung an der Küste mit Meer und Strand" style="background:linear-gradient(#9ab8d4,#dbe6ee 50%,#4f7aa0)"><b>Erholung</b><i>an der Küste</i></a>
  </div>
  <form class="filter" style="margin-top:38px">
    <label>Dauer</label><div class="select">1 – 5 Tage</div>
    <label>Preis</label><div class="select">0 – 100 Euro</div>
    <label>Verpflegung</label><div class="select">--- Auswahl ---</div>
    <div class="btn">suchen</div>
    <div class="or">oder</div>
    <div class="offer-no">Angebotsnummer</div>
    <div class="field"></div>
    <div class="btn">suchen</div>
  </form>
</aside>

<aside class="box" style="left:891px;top:821px;width:204px;height:130px">
  <div class="box-head">quilmar Telefon Support</div>
  <p style="padding:9px 8px;line-height:15px">Sie möchten dieses Angebot telefonisch buchen oder wünschen eine persönliche Beratung? Sie erreichen uns von Montag-Freitag von</p>
</aside>
</body>
</html>
```